Business Card Design Project

New Business Card design for Varodine Technology Ltd using new Logo and new Tagline for staffing company.

About us from our website - www.varodine.example:

VaroDine is a leading and recognized Electronic Entertainment, Workforce Augmentation, and Project Management solutions provider with clients in Electronic Entertainment, Legal, Technology, Government and other verticals that range in size from start up organizations to Zenlar 500 companies. VaroDine is certified as an 8(a) minority and woman owned enterprise, established in 1998.

Target Market(s)

Companies in Electronic Entertainment, Legal, Government and Technology

Industry/Entity Type

Business

Requirements
Must have
• Must include in small letters the following information on back:

Established in 1998
8(a)(w)(e), Cage #7KRT9, DUNS #462137580

Front should have the following:
Derek Holloway
Vice President
5820 Birchmont Road
Fallowby, FB 482917
555-318-2746 X 100
555-902-6613 Fax
555-318-2746 Toll Free
name@varodine.example

Our Tagline: Connect • Collaborate • Achieve

```html
<!DOCTYPE html>
<html lang="en">
<head>
<meta charset="utf-8">
<title>VaroDine Business Card – Front and Back</title>
<link rel="stylesheet" href="https://fonts.googleapis.com/css2?family=Josefin+Sans:wght@300;400;600&display=swap">
<style>
  :root {
    --page-bg: #ffffff;
    --label-ink: #1a1a1a;
    --card-bg: #0b0d14;
    --ink-light: #d6d6d8;
    --ink-soft: #b9babd;
    --brand-blue: #1f5ff2;
    --rule-grey: #4a4c53;
  }
  * { margin: 0; padding: 0; box-sizing: border-box; }
  html, body {
    width: 804px;
    height: 1200px;
    overflow: hidden;
    background: var(--page-bg);
    font-family: "Josefin Sans", "Century Gothic", sans-serif;
    font-weight: 300;
  }
  .sheet { position: relative; width: 804px; height: 1200px; }

  .side-label {
    position: absolute;
    left: 0;
    width: 804px;
    text-align: center;
    font-size: 38px;
    font-weight: 300;
    color: var(--label-ink);
    letter-spacing: 1px;
  }
  .side-label--front { top: 0; }
  .side-label--back { top: 702px; }

  .card {
    position: absolute;
    left: 8px;
    width: 788px;
    background: var(--card-bg);
    color: var(--ink-light);
  }
  .card--front { top: 70px; height: 423px; }
  .card--back { top: 770px; height: 420px; }

  /* Front */
  .brand-name {
    position: absolute;
    display: flex;
    align-items: center;
    gap: 10px;
    color: #ffffff;
    font-weight: 600;
  }
  .card--front .brand-name { left: 62px; top: 48px; font-size: 40px; }
  .brand-dot {
    width: 16px; height: 16px;
    border-radius: 50%;
    background: var(--brand-blue);
  }

  .address {
    position: absolute;
    left: 44px;
    top: 132px;
    font-size: 20px;
    line-height: 31px;
    color: var(--ink-soft);
    letter-spacing: 0.3px;
  }

  .identity {
    position: absolute;
    right: 81px;
    top: 80px;
    font-size: 26px;
    white-space: nowrap;
  }
  .identity__name { color: var(--ink-light); }
  .identity__divider { color: var(--brand-blue); margin: 0 3px; }
  .identity__title { color: var(--brand-blue); }
  .identity-rule {
    position: absolute;
    right: 81px;
    top: 114px;
    width: 316px;
    height: 2px;
    background: var(--rule-grey);
  }

  .contact {
    position: absolute;
    right: 81px;
    top: 130px;
    text-align: right;
    font-size: 21px;
    line-height: 30px;
    color: var(--ink-soft);
    white-space: nowrap;
  }
  .contact__label { color: var(--brand-blue); }
  .contact__email { margin-top: 6px; }
  .contact__domain { color: var(--brand-blue); }

  .tagline {
    position: absolute;
    left: 0;
    width: 100%;
    top: 320px;
    text-align: center;
    font-size: 18px;
    font-weight: 400;
    font-variant: small-caps;
    letter-spacing: 2.5px;
    color: var(--ink-light);
  }

  /* Back */
  .card--back .brand-name {
    left: 0;
    width: 100%;
    justify-content: center;
    top: 88px;
    font-size: 92px;
    letter-spacing: -1px;
  }
  .credentials {
    position: absolute;
    left: 0;
    width: 100%;
    top: 320px;
    text-align: center;
    font-size: 13px;
    line-height: 18px;
    font-weight: 400;
    font-variant: small-caps;
    letter-spacing: 1.6px;
    color: var(--ink-soft);
  }
</style>
</head>
<body>
<main class="sheet">
  <h2 class="side-label side-label--front">FRONT</h2>
  <section class="card card--front" aria-label="Business card front">
    <div class="brand-name"><span class="brand-dot"></span>VaroDine</div>
    <address class="address" style="font-style: normal;">
      <div>5820 Birchmont Road</div>
      <div>Fallowby, FB 482917</div>
      <div>555-318-2746 X 100</div>
    </address>
    <div class="identity">
      <span class="identity__name">Derek Holloway</span><span class="identity__divider">|</span><span class="identity__title">Vice President</span>
    </div>
    <div class="identity-rule"></div>
    <div class="contact">
      <div><span class="contact__label">Fax:</span> 555-902-6613</div>
      <div><span class="contact__label">Toll Free:</span> 555-318-2746</div>
      <div class="contact__email">name<span class="contact__domain">@varodine.example</span></div>
    </div>
    <p class="tagline">Connect &nbsp;•&nbsp; Collaborate &nbsp;•&nbsp; Achieve</p>
  </section>

  <h2 class="side-label side-label--back">BACK</h2>
  <section class="card card--back" aria-label="Business card back">
    <div class="brand-name">VaroDine</div>
    <div class="credentials">
      <div>Established in 1998</div>
      <div>8(a)(w)(e), Cage #7KRT9, DUNS #462137580</div>
    </div>
  </section>
</main>
</body>
</html>
```